Original business card of a small accounting firm

My firm specializes in accounting and taxes for small businesses. I'm looking for an original and creative business card as a marketing tool to give to prospective clients; however since we are a professional firm the card must also appear professional. I'm uploading a few examples of what I believe may fit my needs. Please feel free to use them as a jumping off point. Lastly, I'm uploading the company logo which I'd like to be the focal point on the back of the card and somewhat incorporated on the front on a smaller scale. I hope my description was helpful.
Target Market(s)
Tax clients and small businesses
Industry/Entity Type
Accounting
Contact Information for Business Card
Gerald Whitcombe
Certified Public Accountant │President
Whitcombe Advisors
T│ (555) 417-2863
Email│GWhitcombe@WhitcombeAdvisors.example
Look and feel
Each slider illustrates characteristics of the customer's brand and the style your logo design should communicate.

```html
<!DOCTYPE html>
<html lang="en">
<head>
<meta charset="utf-8">
<title>Whitcombe Advisors – Business Card Front</title>
<link rel="stylesheet" href="https://fonts.googleapis.com/css2?family=Play:wght@400;700&display=swap">
<style>
  :root {
    --stage: #e9eaec;
    --card-top: #ffffff;
    --card-bottom: #e6e7e9;
    --brand-blue: #3f5fc0;
    --band-blue-deep: #3550b8;
    --band-blue-light: #3aa2e3;
    --icon-blue: #2f3fa8;
    --name-blue: #3a4fb0;
    --ink: #2b2b2e;
    --muted: #6b6d72;
    --rule-grey: #8a8c90;
  }
  * { box-sizing: border-box; margin: 0; padding: 0; }
  html, body { width: 1200px; height: 800px; overflow: hidden; }
  body {
    background: var(--stage);
    font-family: "Play", sans-serif;
    position: relative;
  }
  .card {
    position: absolute;
    left: 75px; top: 100px;
    width: 1050px; height: 600px;
    background: linear-gradient(160deg, var(--card-top) 30%, var(--card-bottom) 100%);
    box-shadow: 0 10px 30px rgba(0,0,0,0.18);
    overflow: hidden;
  }
  .card__rule {
    position: absolute;
    left: 0; right: 0; top: 498px;
    height: 6px;
    background: var(--rule-grey);
  }
  .card__band {
    position: absolute;
    left: 0; right: 0; bottom: 0;
    height: 84px;
    background: linear-gradient(90deg, var(--band-blue-deep), var(--band-blue-light) 55%, var(--band-blue-deep));
  }
  .brand {
    position: absolute;
    left: 40px; top: 225px;
    width: 470px;
    text-align: center;
  }
  .brand__mark {
    display: inline-flex;
    align-items: center;
    gap: 14px;
    white-space: nowrap;
  }
  .brand__square {
    width: 30px; height: 30px;
    background: var(--brand-blue);
    flex: none;
  }
  .brand__name {
    font-size: 36px;
    font-weight: 700;
    color: var(--ink);
    letter-spacing: 0.5px;
  }
  .brand__tagline {
    margin-top: 6px;
    font-size: 15px;
    letter-spacing: 2px;
    text-transform: uppercase;
    color: var(--muted);
    white-space: nowrap;
  }
  .divider {
    position: absolute;
    left: 530px; top: 95px;
    width: 3px; height: 300px;
    background: linear-gradient(180deg, transparent, var(--rule-grey) 20%, var(--ink) 60%, transparent);
  }
  .contact {
    position: absolute;
    left: 570px; top: 80px;
    color: var(--ink);
  }
  .contact__name {
    font-size: 34px;
    font-weight: 700;
    letter-spacing: 1.5px;
    text-transform: uppercase;
    color: var(--name-blue);
  }
  .contact__title {
    font-size: 24px;
    margin-top: 2px;
  }
  .contact__address {
    margin-top: 30px;
    font-size: 23px;
    line-height: 1.3;
  }
  .contact__list {
    list-style: none;
    margin-top: 28px;
    font-size: 19px;
  }
  .contact__list li {
    display: flex;
    align-items: center;
    gap: 14px;
    height: 37px;
    white-space: nowrap;
  }
  .contact__icon { width: 20px; height: 20px; fill: var(--icon-blue); flex: none; }
</style>
</head>
<body>
  <main class="card">
    <div class="card__rule"></div>
    <div class="card__band" role="img" aria-label="Decorative blue band along the bottom edge of the card"></div>

    <div class="brand">
      <div class="brand__mark">
        <span class="brand__square"></span>
        <span class="brand__name">Whitcombe Advisors</span>
      </div>
      <p class="brand__tagline">Small business accounting and taxes</p>
    </div>

    <div class="divider"></div>

    <section class="contact">
      <h1 class="contact__name">Peter Langford</h1>
      <p class="contact__title">Managing Director</p>
      <p class="contact__address">210, 12th floor, Harbor<br>Lane Road NWK</p>
      <ul class="contact__list">
        <li>
          <svg class="contact__icon" viewBox="0 0 20 20"><path d="M4 2l3 0 2 5-2 1.5c1 2 2.5 3.5 4.5 4.5L13 11l5 2v3c0 1-1 2-2 2C8 18 2 12 2 4c0-1 1-2 2-2z"/></svg>
          <span>555 302 1148</span>
        </li>
        <li>
          <svg class="contact__icon" viewBox="0 0 20 20"><path d="M6 1h8a1 1 0 0 1 1 1v16a1 1 0 0 1-1 1H6a1 1 0 0 1-1-1V2a1 1 0 0 1 1-1zm1 2v12h6V3z"/></svg>
          <span>555 302 1148</span>
        </li>
        <li>
          <svg class="contact__icon" viewBox="0 0 20 20"><path d="M6 2h7v5H6zM3 8h14a1 1 0 0 1 1 1v8a1 1 0 0 1-1 1H3a1 1 0 0 1-1-1V9a1 1 0 0 1 1-1zm2 3v2h4v-2z"/></svg>
          <span>555 302 1148</span>
        </li>
        <li>
          <svg class="contact__icon" viewBox="0 0 20 20"><path d="M2 4h16v12H2zm1.5 1.5L10 11l6.5-5.5z"/></svg>
          <span>name@mailbox.example</span>
        </li>
        <li>
          <svg class="contact__icon" viewBox="0 0 20 20"><path d="M10 1a9 9 0 1 0 0 18 9 9 0 0 0 0-18zm0 2c1 1.2 1.8 3 2 5H8c.2-2 1-3.8 2-5zM3.1 9h3c.1 2 .6 3.7 1.5 5.3A7 7 0 0 1 3.1 11zm0-1A7 7 0 0 1 7.6 3.7C6.7 5.3 6.2 7 6.1 8zm5 1h3.8c-.2 2.2-1 4-1.900 5.4C9 13 8.3 11.2 8.1 9zm5.8 0h3a7 7 0 0 1-4.5 5.3c.9-1.6 1.4-3.3 1.5-5.3zm3-1h-3c-.1-1-.6-2.7-1.5-4.3A7 7 0 0 1 16.9 8z"/></svg>
          <span>www.yoursitename.example</span>
        </li>
      </ul>
    </section>
  </main>
</body>
</html>
```